Business card design incorporating discount offer

We are a trade services company and we need a double sided business card that is going to be used by our tradesmen to give to customers on completion of their jobs.

Below are the key elements of the card that we would like to include:

-Main logo with text 'Expert Property Care' underneath.
-Up to 12 smaller icon logos with text 'Your local all-trade experts' to emphasise the point that we cover all the trades
-Discount offer - 10% discount
-Telephone number and website address
-Blank space for tradesman to enter his/her name
-Request for customer feedback with feedback url

This business card will be printed on regular card. In the past we have favoured designs that use a black background but we're open to new ideas.

I have attached a few files:

-A simple wire frame example to show how this card could look with the different elements mentioned above, feel free to use a layout similar to this or come up with something totally different (biz-card.pdf)
-Front and back of a loyalty card the we've used in the past (this card was printed on plastic)
-Front and back of a key fob design that we've previously used (this card was printed on plastic)
-A logo file with the 12 small icons and the main logo image

If you need further images or information please ask.

```html
<!DOCTYPE html>
<html lang="en">
<head>
<meta charset="utf-8">
<title>KRV Business Card – Both Sides</title>
<link rel="stylesheet" href="https://fonts.googleapis.com/css2?family=Open+Sans:wght@400;600;700;800&display=swap">
<style>
  :root {
    --brand-blue: #1a84cf;
    --brand-blue-dark: #0f5f9c;
    --card-black: #161616;
    --card-black-soft: #222222;
    --card-white: #ffffff;
    --ink-dark: #111111;
    --page-bg: #e6e4e0;
  }
  * { box-sizing: border-box; margin: 0; padding: 0; }
  html, body {
    width: 1200px;
    height: 998px;
    overflow: hidden;
    background: var(--page-bg);
    font-family: "Open Sans", Arial, sans-serif;
  }
  .canvas {
    position: relative;
    width: 1200px;
    height: 998px;
  }
  .card {
    position: absolute;
    width: 700px;
    height: 450px;
    border-radius: 34px;
    overflow: hidden;
    box-shadow: 0 6px 18px rgba(0,0,0,0.18);
  }

  /* ---------- Reverse side: discount card ---------- */
  .card--offer {
    left: 60px;
    top: 28px;
    background: linear-gradient(180deg, var(--card-black-soft), var(--card-black));
    display: flex;
  }
  .offer-panel {
    width: 200px;
    height: 100%;
    background: var(--card-white);
    border-right: 22px solid var(--brand-blue);
    padding: 78px 0 0 0;
    text-align: center;
    color: var(--brand-blue);
    flex-shrink: 0;
  }
  .offer-panel__figure {
    font-size: 74px;
    font-weight: 700;
    line-height: 1;
    letter-spacing: -2px;
  }
  .offer-panel__caption {
    font-size: 21px;
    font-weight: 700;
    line-height: 1.15;
    margin-top: 6px;
  }
  .offer-panel__tagline {
    font-size: 27px;
    font-weight: 700;
    line-height: 1.2;
    margin-top: 62px;
  }
  .offer-details {
    flex: 1;
    padding: 40px 40px 0 40px;
    color: var(--card-white);
  }
  .tradesman-label {
    font-size: 17px;
    font-weight: 600;
    margin-left: 6px;
  }
  .tradesman-field {
    height: 46px;
    margin-top: 4px;
    background: var(--card-white);
    border: 3px solid var(--brand-blue);
    border-radius: 7px;
  }
  .trade-grid {
    display: grid;
    grid-template-columns: repeat(5, 66px);
    gap: 20px 22px;
    margin: 30px 0 0 8px;
  }
  .trade-tile {
    width: 66px;
    height: 66px;
    border-radius: 14px;
    background: linear-gradient(180deg, #3aa3ea, var(--brand-blue-dark));
    border: 2px solid #5fb7f0;
  }
  .feedback {
    margin-top: 26px;
    text-align: center;
    font-size: 17px;
    line-height: 1.3;
  }

  /* ---------- Front side: main card ---------- */
  .card--main {
    left: 440px;
    top: 518px;
    background: var(--card-black);
  }
  .main-top {
    height: 236px;
    background: var(--card-white);
    border-bottom: 14px solid var(--brand-blue);
    display: flex;
    flex-direction: column;
    align-items: center;
    padding-top: 44px;
  }
  .brand {
    display: flex;
    align-items: center;
    gap: 18px;
  }
  .brand__mark {
    width: 64px;
    height: 64px;
    border-radius: 50%;
    background: var(--brand-blue);
  }
  .brand__name {
    font-size: 84px;
    font-weight: 800;
    line-height: 1;
    color: var(--ink-dark);
    letter-spacing: 1px;
  }
  .brand__strapline {
    margin-top: 26px;
    font-size: 29px;
    font-weight: 700;
    color: var(--ink-dark);
  }
  .main-bottom {
    display: flex;
    align-items: center;
    height: 200px;
    padding: 0 50px 0 48px;
  }
  .app-tile {
    width: 100px;
    height: 100px;
    border-radius: 20px;
    background: linear-gradient(180deg, #3aa3ea, var(--brand-blue-dark));
    border: 3px solid #5fb7f0;
    flex-shrink: 0;
  }
  .contact {
    margin-left: auto;
    text-align: left;
    color: var(--card-white);
    font-weight: 700;
    font-size: 34px;
    line-height: 1.4;
  }
</style>
</head>
<body>
<main class="canvas">

  <section class="card card--offer" aria-label="Card reverse: discount offer">
    <div class="offer-panel">
      <p class="offer-panel__figure">10%</p>
      <p class="offer-panel__caption">Discount with<br>this card</p>
      <p class="offer-panel__tagline">Your local<br>all-trade<br>experts!</p>
    </div>
    <div class="offer-details">
      <p class="tradesman-label">Your KRV Tradesman</p>
      <div class="tradesman-field"></div>
      <div class="trade-grid" role="img" aria-label="Ten trade service icons: plumbing, carpentry, drainage, bathrooms, gas, kitchens, decorating, plastering, joinery, electrical">
        <span class="trade-tile"></span><span class="trade-tile"></span><span class="trade-tile"></span><span class="trade-tile"></span><span class="trade-tile"></span>
        <span class="trade-tile"></span><span class="trade-tile"></span><span class="trade-tile"></span><span class="trade-tile"></span><span class="trade-tile"></span>
      </div>
      <p class="feedback">What do you think of our service?<br>Please leave feedback online at<br>www.krv-services.co.uk/feedback.</p>
    </div>
  </section>

  <section class="card card--main" aria-label="Card front: company details">
    <div class="main-top">
      <div class="brand">
        <span class="brand__mark"></span>
        <span class="brand__name">KRV</span>
      </div>
      <p class="brand__strapline">Expert Property Care</p>
    </div>
    <div class="main-bottom">
      <div class="app-tile" role="img" aria-label="Company app icon"></div>
      <div class="contact">
        <p>0800 123 4567</p>
        <p>krv-services.co.uk</p>
      </div>
    </div>
  </section>

</main>
</body>
</html>
```